Very Simple/Minimal Business Card Design Project

The company operates in the industrial maritime infrastructure sector in Brazil. You can find more information on our website www.navelquor.com.br WE NEED TO LOOK POWERFUL AND SERIOUS
I have attached a copy of the old cards. We would like something more professional / industrial / sexy that also includes the position.

The card can be double sided or not. We would like you to propose as many options.

Thank you
Updates

Many thanks, do let me know if you have any questions. I am under a lot of time pressure to try and have them printed over the next days or so.

Please could you use the following information

for the address: Rua Tapiraçu, 418 - Centro, Rio de Janeiro, 20135-070, Brasil

for the mobile: +55 21 8372 9041
for the landline: +55 21 4067 3859

and position:  Diretor Geral

Thakn you

Target Market(s)

Shipowners, bankers, industrial companies

Industry/Entity Type

Industrial

Requirements
Must have
• POWERFUL
SERIOUS
SOLID
BIG CORPORATION

```html
<!DOCTYPE html>
<html lang="pt-BR">
<head>
<meta charset="utf-8">
<title>NAVELQUOR – Business Card</title>
<link rel="stylesheet" href="https://fonts.googleapis.com/css2?family=Open+Sans:wght@400;600;700;800&display=swap">
<style>
  :root {
    --navy: #2c3566;
    --navy-deep: #263a72;
    --green: #169a4a;
    --white: #ffffff;
    --silver: #b9bcc2;
    --ink: #2c3566;
    --stage: #e6e8ec;
  }
  * { margin: 0; padding: 0; box-sizing: border-box; }
  html, body { width: 1000px; height: 1200px; overflow: hidden; }
  body {
    background: var(--stage);
    font-family: "Open Sans", Arial, sans-serif;
    color: var(--ink);
    position: relative;
  }
  .card {
    position: absolute;
    left: 100px;
    width: 800px;
    height: 457px;
    background: var(--white);
    box-shadow: 0 6px 24px rgba(0,0,0,0.18);
    overflow: hidden;
  }
  .card--front { top: 100px; }
  .card--back { top: 643px; }
  .card__art { position: absolute; inset: 0; }

  /* Front */
  .brand {
    position: absolute;
    left: 210px;
    top: 190px;
    display: flex;
    align-items: center;
    gap: 16px;
  }
  .brand__square {
    width: 58px;
    height: 58px;
    background: var(--green);
  }
  .brand__name {
    font-size: 64px;
    font-weight: 800;
    color: var(--navy);
    letter-spacing: 1px;
    line-height: 1;
  }
  .website {
    position: absolute;
    left: 400px;
    top: 380px;
    font-size: 19px;
    color: var(--navy);
  }

  /* Back */
  .brand-vertical {
    position: absolute;
    left: 700px;
    top: 228px;
    transform: translate(-50%, -50%) rotate(90deg);
    font-size: 44px;
    font-weight: 800;
    color: var(--white);
    letter-spacing: 1px;
    white-space: nowrap;
  }
  .person {
    position: absolute;
    left: 60px;
    top: 150px;
  }
  .person__name {
    font-size: 38px;
    font-weight: 700;
    color: var(--navy);
    line-height: 1.1;
  }
  .person__role {
    font-size: 19px;
    color: var(--navy);
    margin-top: 2px;
  }
  .contacts {
    position: absolute;
    left: 60px;
    top: 280px;
    list-style: none;
    font-size: 16px;
    color: var(--navy);
    line-height: 1.25;
  }
  .contacts li {
    display: flex;
    align-items: flex-start;
    gap: 10px;
  }
  .contacts li + li { margin-top: 6px; }
  .contacts .gap { margin-top: 18px; }
  .contacts svg { width: 18px; height: 18px; flex: none; margin-top: 1px; }
  .phone-table td { padding: 0 10px 0 0; }
</style>
</head>
<body>

  <section class="card card--front" aria-label="Card front">
    <svg class="card__art" viewBox="0 0 800 457" preserveAspectRatio="none" aria-hidden="true">
      <defs>
        <linearGradient id="band" x1="0" y1="0" x2="0" y2="1">
          <stop offset="0" stop-color="#2c3566"/>
          <stop offset="0.5" stop-color="#169a4a"/>
          <stop offset="1" stop-color="#2c3566"/>
        </linearGradient>
      </defs>
      <path d="M0,0 H120 Q40,230 170,457 H0 Z" fill="url(#band)"/>
      <path d="M610,0 Q780,230 690,457 H800 V0 Z" fill="url(#band)"/>
    </svg>
    <div class="brand">
      <span class="brand__square"></span>
      <span class="brand__name">NAVELQUOR</span>
    </div>
    <p class="website">www.navelquor.com.br</p>
  </section>

  <section class="card card--back" aria-label="Card back">
    <svg class="card__art" viewBox="0 0 800 457" preserveAspectRatio="none" aria-hidden="true">
      <defs>
        <linearGradient id="panel" x1="0" y1="0" x2="0" y2="1">
          <stop offset="0" stop-color="#2c3566"/>
          <stop offset="0.5" stop-color="#169a4a"/>
          <stop offset="1" stop-color="#2c3566"/>
        </linearGradient>
      </defs>
      <path d="M590,0 Q720,230 600,457 H800 V0 Z" fill="url(#panel)"/>
      <path d="M590,0 Q720,230 600,457" fill="none" stroke="#b9bcc2" stroke-width="6"/>
    </svg>

    <p class="brand-vertical">NAVELQUOR</p>

    <div class="person">
      <h1 class="person__name">Leopold Farrant</h1>
      <p class="person__role">Diretor Geral</p>
    </div>

    <ul class="contacts">
      <li>
        <svg viewBox="0 0 20 20" aria-hidden="true"><path d="M10 2 L19 10 H16 V18 H12 V13 H8 V18 H4 V10 H1 Z" fill="#169a4a"/></svg>
        <span>Rua Tapiraçu, 418 - Centro,<br>Rio de Janeiro, 20135-070, Brasil</span>
      </li>
      <li class="gap">
        <svg viewBox="0 0 20 20" aria-hidden="true"><circle cx="10" cy="10" r="8.5" fill="none" stroke="#169a4a" stroke-width="2"/><path d="M6.5 6 l2 -0.5 1 2.5 -1.2 1 a6 6 0 0 0 2.7 2.7 l1 -1.2 2.5 1 -0.5 2 c-4 0.5 -8 -3.5 -7.5 -7.5z" fill="#169a4a"/></svg>
        <table class="phone-table"><tr><td>landline:</td><td>+55 21 4067 3859</td></tr><tr><td>mobile:</td><td>+55 21 8372 9041</td></tr></table>
      </li>
      <li>
        <svg viewBox="0 0 20 20" aria-hidden="true"><rect x="1" y="4" width="18" height="12" fill="none" stroke="#169a4a" stroke-width="2"/><path d="M1 4 L10 11 L19 4" fill="none" stroke="#169a4a" stroke-width="2"/></svg>
        <span>geral@navelquor.com.br</span>
      </li>
    </ul>
  </section>

</body>
</html>
```